Cloud-based Health 2.0 Web Site

We need the overall look and feel for a new cloud-based Health 2.0 web site where health professionals can manage and interact with their patients/clients.

The plan is to generate a landing page that can grab the attention of health professionals (doctors, nurses, personal trainers, etc...). This page should have an attractive "Sign Up for Free" or similar button/message, as well as a login section for users already registered. We currently have a view on having a number of messages displayed, either as a slider or as separate areas on the page (decision is up for grabs).

Secondly, we need a standard "framework" for all the other pages which will be accessible once the user has authenticated with a clean, airy and spacious feel. This will provide styling for standard elements (input boxes, checkboxes, etc...) as well as a given layout, possibly 3 columns (fixed-fluid-fixed) although we leave this to the designer's choice.

We want to stress the importance of the Cloud, as well as make users feel like "this is the place to be if you're a modern, tech savvy health professional". Also of high importance is to show that this is a secure place, where data is accessible from anywhere yet also highly protected.

This project is going to provide long-term work for the winner and possibly those we consider close runner ups, so if you guys are interested in grabbing our attention so you can become our designer of choice, this is your chance!

Standard pages we are looking to receive after the selection process:

* Landing page
* Health Professional Profile Page (personal details, professional details, photo...)
* Patient list / Patient Management page
* Patient profile (details, health details...)
* Generic "item" management page (item refers to documents, images, contacts, etc...)

The logo for the site/product is also up for grabs, and a bonus payment can be given if you provide one that both matches the style of the site whilst being one that could be reused for mobile app icons, etc...

The site name is "vornatik" (all lower-case) for those of you wanting to work on the logo part. As I said before, the logo should contain a component that could be use as the recognisable icon in a mobile phone app. Something that can be easily identified in both the site and the app that connects them together.

vornatik is made up of two parts (vorn + atik), and you might want to consider differentiating them by the use of colour, fonts or however you think appropriate.

New sample screen-shots of the existing functionality have been uploaded to help you mock up some screens.

PLEASE NOTE: This are to be used for content/widget design only! The layout of how these are represented, e.g. accordion, slider, tree, list... is entirely up to you! Don't guide your layout based on these screen-shots, unless you think they are the way to go, of course. 

We want your creative input, so please innovate! :)

Thanks!

Target Market(s)

Health Professionals

Industry/Entity Type

Health

Requirements
Must have
• * A landing page that grabs the users attention but is "different" from the rest of pages (although within the same design/style parameters)

* A generic page framework for the rest of the pages (style guide)
Nice to have
• A modern and clean logo to go with the site. If the logo is selected, this can result in a bonus payment to be decided.

```html
<!DOCTYPE html>
<html lang="en">
<head>
<meta charset="utf-8">
<title>meridio – health 2.0 in the cloud</title>
<link rel="stylesheet" href="https://fonts.googleapis.com/css2?family=Arvo:wght@700&family=Handlee&display=swap">
<style>
:root{
  --doctor-blue:#1b6fc0;
  --doctor-blue-dark:#155ea6;
  --nurse-teal:#31d0d4;
  --nurse-teal-dark:#27bcc0;
  --trainer-gold:#f2b600;
  --trainer-gold-dark:#e2a900;
  --logo-grey:#bdbdbd;
  --link-blue:#5bb7d9;
  --text-grey:#555555;
  --footer-grey:#999999;
  --bar-border:#cfcfcf;
  --arrow-blue:#1f93d8;
  --white:#ffffff;
}
*{margin:0;padding:0;box-sizing:border-box}
html,body{width:1200px;height:900px;overflow:hidden;background:var(--white)}
body{position:relative;font-family:Arial,Helvetica,sans-serif}

.site-logo{position:absolute;left:20px;top:14px;font-family:'Arvo',serif;font-weight:700;font-size:32px;color:var(--logo-grey);letter-spacing:0.5px}
.login-link{position:absolute;right:58px;top:32px;font-family:'Handlee',cursive;font-size:21px;color:var(--link-blue);text-decoration:none}

.audience-columns{position:absolute;left:0;top:69px;width:1160px;height:660px;display:flex;gap:2px}
.audience{position:relative;flex:1;height:100%;color:var(--white)}
.audience--doctors{background:var(--doctor-blue)}
.audience--nurses{background:var(--nurse-teal)}
.audience--trainers{background:var(--trainer-gold)}

.audience__photo{position:absolute;left:19px;top:21px;width:344px;height:346px}
.audience--doctors .audience__photo{background:linear-gradient(135deg,#f4f6f8 0%,#dfe6ee 55%,#8fb6dc 100%)}
.audience--nurses .audience__photo{background:linear-gradient(180deg,#f7f7f7 0%,#c9d9ea 55%,#2f6fbf 100%)}
.audience--trainers .audience__photo{left:21px;background:linear-gradient(135deg,#4a5470 0%,#c8ccd6 45%,#eeeeee 100%)}

.audience__title{position:absolute;left:35px;top:399px;font-size:18.5px;font-weight:bold}
.audience--nurses .audience__title{left:34px}
.audience--trainers .audience__title{left:21px}
.audience__text{position:absolute;left:35px;top:434px;width:332px;font-size:14px;line-height:20px}
.audience--nurses .audience__text{left:34px;width:325px}
.audience--trainers .audience__text{left:21px;top:442px;width:326px}

.enter-button{position:absolute;left:32px;top:613px;width:308px;height:29px;border-radius:15px;display:flex;align-items:center;font-size:12px;text-decoration:none;color:var(--white)}
.audience--doctors .enter-button{background:var(--doctor-blue-dark);box-shadow:inset 0 1px 2px rgba(0,0,0,.25)}
.audience--nurses .enter-button{background:var(--nurse-teal-dark);box-shadow:inset 0 1px 2px rgba(0,0,0,.15)}
.audience--trainers .enter-button{left:26px;background:var(--trainer-gold-dark);box-shadow:inset 0 1px 2px rgba(0,0,0,.15)}
.enter-button__label{position:absolute;left:180px}
.audience--trainers .enter-button__label{left:166px}
.enter-button__dot{position:absolute;right:18px;width:10px;height:10px;border-radius:50%;background:rgba(255,255,255,.35)}
.enter-button__icon{position:absolute;left:118px;bottom:0;width:48px;height:55px;border-radius:24px 24px 8px 8px;background:linear-gradient(180deg,#e8edf2,#9aa7b4)}
.audience--trainers .enter-button__icon{left:116px;bottom:2px;width:40px;height:28px;border-radius:6px;background:linear-gradient(180deg,#444,#111)}

.signup-bar{position:absolute;left:0;top:744px;width:1161px;height:83px;background:linear-gradient(180deg,#ffffff 0%,#f3f3f3 100%);border:1px solid var(--bar-border);border-left:none}
.signup-bar__label{position:absolute;left:21px;top:28px;font-size:19px;color:var(--text-grey)}
.signup-bar__input{position:absolute;left:129px;top:27px;width:280px;height:27px;border:none;background:linear-gradient(180deg,#e6e6e6,#f9f9f9);padding-left:26px;font-size:12px;color:#444;font-family:Arial,Helvetica,sans-serif}
.signup-bar__submit{position:absolute;left:421px;top:31px;width:20px;height:20px;border-radius:3px;background:var(--arrow-blue);border:none}
.signup-bar__submit svg{display:block;margin:4px auto}

.social{position:absolute;left:572px;top:25px;display:flex;align-items:center;gap:5px;font-family:'Handlee',cursive;font-size:15px;color:var(--text-grey)}
.social__circle{width:34px;height:34px;border-radius:50%}
.social__circle--one{background:#1c4fa0;margin-left:4px}
.social__circle--two{background:#4fb6e8}

.main-nav{position:absolute;right:20px;top:22px;display:flex;font-family:'Handlee',cursive;font-size:20px}
.main-nav a{color:var(--text-grey);text-decoration:none;padding:0 16px;border-left:1px solid #ddd}
.main-nav a:first-child{border-left:none}
.main-nav a:last-child{padding-right:0}

.copyright{position:absolute;right:40px;top:836px;font-size:12.5px;color:var(--footer-grey)}
</style>
</head>
<body>

<header>
  <div class="site-logo">meridio.</div>
  <a class="login-link" href="#">login here</a>
</header>

<main class="audience-columns">
  <section class="audience audience--doctors">
    <div class="audience__photo" role="img" aria-label="Doctor in white coat and blue gloves writing on a tablet, stethoscope around neck"></div>
    <h2 class="audience__title">Health 2.0</h2>
    <p class="audience__text">Applying new technologies to solve the problem of health management has been the dream of many for a long time. With today's technology we are closer than ever to achieve this dream, and vornatik represents a collection of unique technologies and ideas that will revolutionaise the way people think, care for and manage health.</p>
    <a class="enter-button" href="#">
      <span class="enter-button__icon" role="img" aria-label="Doctor avatar icon"></span>
      <span class="enter-button__label">doctors enter here</span>
      <span class="enter-button__dot"></span>
    </a>
  </section>

  <section class="audience audience--nurses">
    <div class="audience__photo" role="img" aria-label="Smiling nurse in blue scrubs holding a clipboard"></div>
    <h2 class="audience__title">Secuirity</h2>
    <p class="audience__text">When online, nothing is more important that security, especially when dealing with health information. vorn-atik is designed from the ground up to be secure and to protect data in a number of different ways to ensure both strong access and data records anonymity.</p>
    <a class="enter-button" href="#">
      <span class="enter-button__icon" role="img" aria-label="Nurse avatar icon"></span>
      <span class="enter-button__label">nrurses enter here</span>
      <span class="enter-button__dot"></span>
    </a>
  </section>

  <section class="audience audience--trainers">
    <div class="audience__photo" role="img" aria-label="Stethoscope lying on a printed medical test report"></div>
    <h2 class="audience__title">Cloud-based</h2>
    <p class="audience__text">meridio represents a small part of the advanced health 2.0 engine that is vornatik and therefore it is designed and built for the Cloud. Data is safely stored in the cloud and users can accessed it from anywhere as long as they are authenticated and connected over a secure channel.</p>
    <a class="enter-button" href="#">
      <span class="enter-button__icon" role="img" aria-label="Medical bag icon"></span>
      <span class="enter-button__label">trainers enter here</span>
      <span class="enter-button__dot"></span>
    </a>
  </section>
</main>

<footer>
  <form class="signup-bar">
    <label class="signup-bar__label" for="signup-email">sign up here</label>
    <input class="signup-bar__input" id="signup-email" type="email" placeholder="enter email address">
    <button class="signup-bar__submit" type="submit" aria-label="Sign up">
      <svg width="12" height="12" viewBox="0 0 12 12"><path d="M1 6h8M6 2.5L9.5 6 6 9.5" stroke="#fff" stroke-width="2" fill="none"/></svg>
    </button>
    <div class="social">
      <span>connect with us</span>
      <span class="social__circle social__circle--one" aria-label="Social network one"></span>
      <span class="social__circle social__circle--two" aria-label="Social network two"></span>
    </div>
    <nav class="main-nav">
      <a href="#">home</a>
      <a href="#">about us</a>
      <a href="#">contact us</a>
    </nav>
  </form>
  <p class="copyright">2012 - corvane ltd.</p>
</footer>

</body>
</html>
```